Book cover for book titled The Quiet Harbor's Drift Ledger

Need a book cover for a book size 5.25 x 8.
Title: The Quiet Harbor's Drift Ledger
Subtitle: 40 Habits You Might Shed on the Road to a Calmer Year in the Season of Change
Author: Dr. Marvin T. Okafor
Foreword by Leopold Vantrease, Ph.D.
The book cover should be white. I have uploaded 2 photos. The closeup with the hat should go on the front with the text. The one in the chair should go on the back. It will be the only thing on the back.

```html
<!DOCTYPE html>
<html lang="en">
<head>
<meta charset="utf-8">
<title>The Quiet Harbor's Drift Ledger — Cover Spread</title>
<link href="https://fonts.googleapis.com/css2?family=Cinzel:wght@400;600;700&family=Crimson+Text:ital,wght@0,600;0,700;1,600&display=swap" rel="stylesheet">
<style>
  :root {
    --page: #ffffff;
    --spine: #d9d9de;
    --spine-ink: #3b3d5c;
    --title-red: #cc1f45;
    --sub-ink: #1e1e24;
    --photo-light: #f4f1ea;
    --photo-mid: #6f6e72;
    --photo-dark: #141a2a;
    --on-photo: #ffffff;
  }
  html, body {
    margin: 0;
    width: 1200px;
    height: 1200px;
    overflow: hidden;
    background: var(--page);
  }
  .spread {
    position: absolute;
    left: 81px;
    top: 229px;
    width: 1040px;
    height: 744px;
    display: flex;
    background: var(--page);
    box-shadow: 0 0 6px rgba(0,0,0,0.35), 2px 3px 8px rgba(0,0,0,0.25);
  }
  .back-cover {
    position: relative;
    width: 489px;
    height: 100%;
    background: var(--page);
  }
  .back-photo {
    position: absolute;
    left: 103px;
    top: 213px;
    width: 292px;
    height: 358px;
    background: radial-gradient(ellipse at 50% 45%, #9a9aa0 0%, #d8d6d2 55%, rgba(255,255,255,0) 80%);
  }
  .spine {
    position: relative;
    width: 62px;
    height: 100%;
    background: var(--spine);
  }
  .spine-title,
  .spine-author {
    position: absolute;
    left: 50%;
    writing-mode: vertical-rl;
    transform: translateX(-50%);
    color: var(--spine-ink);
    font-family: "Cinzel", serif;
    white-space: nowrap;
  }
  .spine-title {
    top: 48px;
    font-size: 20px;
    letter-spacing: 0.8px;
  }
  .spine-author {
    top: 471px;
    font-size: 16px;
    letter-spacing: 0.6px;
  }
  .front-cover {
    position: relative;
    width: 489px;
    height: 100%;
    background: var(--page);
    overflow: hidden;
  }
  .front-photo {
    position: absolute;
    left: 0;
    top: 238px;
    width: 100%;
    height: 506px;
    background: linear-gradient(180deg,
      var(--photo-light) 0%,
      #d9c38f 20%,
      #8a6f5e 45%,
      var(--photo-mid) 62%,
      #2a2f40 82%,
      var(--photo-dark) 100%);
  }
  .title {
    position: absolute;
    left: 0;
    top: 45px;
    width: 100%;
    margin: 0;
    text-align: center;
    color: var(--title-red);
    font-family: "Cinzel", serif;
    font-weight: 600;
    line-height: 1;
  }
  .title-line-1 {
    display: block;
    font-size: 42px;
    letter-spacing: -0.5px;
  }
  .title-line-2 {
    display: block;
    font-size: 66px;
    letter-spacing: -1px;
    margin-top: -4px;
  }
  .subtitle {
    position: absolute;
    left: 10px;
    right: 10px;
    top: 180px;
    margin: 0;
    text-align: center;
    color: var(--sub-ink);
    font-family: "Crimson Text", serif;
    font-style: italic;
    font-weight: 600;
    font-size: 15px;
    line-height: 18px;
    letter-spacing: 1px;
    white-space: nowrap;
  }
  .author {
    position: absolute;
    left: 0;
    width: 100%;
    top: 645px;
    margin: 0;
    text-align: center;
    color: var(--on-photo);
    font-family: "Cinzel", serif;
    font-weight: 400;
    font-size: 32px;
    letter-spacing: 0.5px;
  }
  .foreword {
    position: absolute;
    left: 0;
    width: 100%;
    top: 690px;
    margin: 0;
    text-align: center;
    color: var(--on-photo);
    font-family: "Crimson Text", serif;
    font-weight: 700;
    font-size: 21px;
    letter-spacing: 0.5px;
  }
</style>
</head>
<body>
  <div class="spread">
    <section class="back-cover">
      <div class="back-photo" role="img" aria-label="Photo of the author seated in a white armchair wearing a dark jacket, jeans, red sneakers and a face mask, a straw boater hat at his feet"></div>
    </section>

    <section class="spine">
      <span class="spine-title">The Quiet Harbor's Drift Ledger</span>
      <span class="spine-author">Dr. Marvin T. Okafor</span>
    </section>

    <section class="front-cover">
      <div class="front-photo" role="img" aria-label="Close-up photo of the author in a straw boater hat with a navy and red band, tinted glasses and a grey face mask"></div>
      <h1 class="title">
        <span class="title-line-1">The Quiet Harbor's</span>
        <span class="title-line-2">Drift Ledger</span>
      </h1>
      <p class="subtitle">40 Habits You Might Shed on the Road to a Calmer<br>Year in the Season of Change</p>
      <p class="author">Dr. Marvin T. Okafor</p>
      <p class="foreword">Foreword by Leopold Vantrease, Ph.D.</p>
    </section>
  </div>
</body>
</html>
```